Harbor Lantern Productions Business Logo and Card Design

PLEASE LIMIT your submission to maximum of 2 at a time.
Harbor Lantern Productions provides video production services, and produces videos, that help people connect in the spirit of unity and peace.Primarily I am looking for a logo that is simple to remember but the concept is fairly complex. The concept of the logo is a peace dove with an olive branch in it's mouth has it's wings around earth, symbolising that it is protecting earth with peace. If possible I'd like this logo done and delivered in high quality vector format, so I can use it for banners etc.Then the business card I just want a simple white card with the logo in the middle and contact info under the logo. Open to suggestions if you think there should be anything else included, but it must remain simple and uncluttered. Also incorporate something in the logo that says film and video e.g.: film strip or camera lens

Contact Information for Business Card

Harbor Lantern Productions
www.harborlantern.example
teodor@harborlantern.example
+61 478 315 064

Requirements
Must have
• Logo must have the following:
• Peace Dove
• Olive branch
• Earth
• Something about video production (e.g.: film strip or camera lens or anything film related)

```html
<!DOCTYPE html>
<html lang="en">
<head>
<meta charset="utf-8">
<title>Harbor Lantern Productions – Business Card</title>
<link href="https://fonts.googleapis.com/css2?family=Cinzel:wght@400&family=Open+Sans:wght@400&display=swap" rel="stylesheet">
<style>
  :root {
    --backdrop: #000000;
    --card-white: #ffffff;
    --brand-blue: #1f4fe6;
    --wave-blue: #0047ff;
    --wave-blue-light: #4a7dff;
    --accent-red: #b3121c;
    --accent-red-light: #d23a3f;
    --contact-text: #ffffff;
  }
  * { margin: 0; padding: 0; box-sizing: border-box; }
  html, body {
    width: 1200px; height: 993px; overflow: hidden;
    background: var(--backdrop);
  }
  .stage { position: relative; width: 1200px; height: 993px; }
  .business-card {
    position: absolute; left: 165px; top: 232px;
    width: 878px; height: 540px;
    background: var(--card-white);
    overflow: hidden;
  }
  .card-waves { position: absolute; inset: 0; width: 100%; height: 100%; }
  .brand-lockup {
    position: absolute; left: 170px; top: 48px;
    display: flex; align-items: center; gap: 26px;
  }
  .brand-dot {
    width: 62px; height: 62px; border-radius: 50%;
    background: var(--accent-red);
    flex: none;
  }
  .brand-name {
    font-family: "Cinzel", serif; font-weight: 400;
    color: var(--brand-blue);
    line-height: 1;
  }
  .brand-name .brand-main { display: block; font-size: 50px; letter-spacing: 1px; }
  .brand-name .brand-sub { display: block; font-size: 25px; letter-spacing: 9px; margin-top: 8px; padding-left: 4px; }
  .person-name {
    position: absolute; left: 148px; top: 226px;
    font-family: "Cinzel", serif; font-weight: 400;
    font-size: 38px; letter-spacing: 1px;
    color: var(--brand-blue);
  }
  .contact-list {
    position: absolute; left: 138px; top: 380px;
    list-style: none;
    font-family: "Open Sans", sans-serif; font-size: 32px;
    color: var(--contact-text);
  }
  .contact-item { display: flex; align-items: center; height: 43px; }
  .contact-icon { width: 26px; height: 26px; margin-right: 26px; flex: none; }
</style>
</head>
<body>
<main class="stage">
  <section class="business-card">
    <svg class="card-waves" viewBox="0 0 884 543" preserveAspectRatio="none" aria-hidden="true">
      <defs>
        <linearGradient id="blueWave" x1="0" y1="1" x2="0.6" y2="0">
          <stop offset="0" stop-color="var(--wave-blue)"/>
          <stop offset="0.15" stop-color="var(--wave-blue-light)"/>
          <stop offset="0.45" stop-color="var(--wave-blue)"/>
        </linearGradient>
        <linearGradient id="redSwoosh" x1="0" y1="0" x2="1" y2="0">
          <stop offset="0" stop-color="var(--accent-red-light)"/>
          <stop offset="0.6" stop-color="var(--accent-red)"/>
        </linearGradient>
      </defs>
      <path d="M0,272 C100,340 250,365 400,352 C560,338 700,262 884,268 L884,543 L0,543 Z" fill="url(#blueWave)"/>
      <path d="M0,195 C40,250 130,292 240,310 C330,325 440,320 532,302 C500,320 440,336 360,340 C230,345 90,320 0,258 Z" fill="url(#redSwoosh)"/>
    </svg>

    <div class="brand-lockup">
      <span class="brand-dot"></span>
      <h1 class="brand-name">
        <span class="brand-main">HARBOR LANTERN</span>
        <span class="brand-sub">PRODUCTIONS</span>
      </h1>
    </div>

    <p class="person-name">TEODOR HALVORSEN</p>

    <ul class="contact-list">
      <li class="contact-item">
        <svg class="contact-icon" viewBox="0 0 26 26" aria-hidden="true">
          <circle cx="13" cy="13" r="10.5" fill="none" stroke="#fff" stroke-width="2.5"/>
          <path d="M6,11 H20 M6,15 H20" stroke="#fff" stroke-width="2"/>
        </svg>
        <span>www.harborlantern.example</span>
      </li>
      <li class="contact-item">
        <svg class="contact-icon" viewBox="0 0 26 26" aria-hidden="true">
          <rect x="2" y="5" width="22" height="16" fill="none" stroke="#fff" stroke-width="2.5"/>
          <path d="M3,6 L13,14 L23,6" fill="none" stroke="#fff" stroke-width="2.5"/>
        </svg>
        <span>teodor@harborlantern.example</span>
      </li>
      <li class="contact-item">
        <svg class="contact-icon" viewBox="0 0 26 26" aria-hidden="true">
          <rect x="5" y="1.5" width="16" height="23" rx="3" fill="none" stroke="#fff" stroke-width="2.5"/>
          <line x1="5" y1="19" x2="21" y2="19" stroke="#fff" stroke-width="2"/>
        </svg>
        <span>+61 478 315 064</span>
      </li>
    </ul>
  </section>
</main>
</body>
</html>
```